Electrical company business card design.

Hi, were an electrical company in Marlowby New Zealand called Quarneth Ltd. We focus mainly on high end residential and commercial so the card would be targeted towards that.
The card will be for myself, i am the director of the company.
Name: Derek Olstow
Position: Director/electrician
Phone: 021 387 9415
Email: derek@quarneth.co.nz
Location: Marlowby
As for colors the the blue color in the logo is preferred, i also don't mind a black background option.
Target Market(s)
High end residential and commercial
Industry/Entity Type
Electrician
Contact Information for Business Card
Name: Derek Olstow Position: Director/Electrician Phone: 021 387 9415, Email: derek@quarneth.co.nz, Location: Marlowby

```html
<!DOCTYPE html>
<html lang="en">
<head>
<meta charset="utf-8">
<title>Quarneth Ltd – Business Card</title>
<link rel="stylesheet" href="https://fonts.googleapis.com/css2?family=Tinos:wght@400;700&display=swap">
<style>
  :root {
    --backdrop: #e5e6e8;
    --brand-blue: #27a8e0;
    --band-dark: #414141;
    --plate-black: #231f20;
    --ink: #1e1e1e;
    --logo-grey: #4d4e50;
    --pin-red: #ed1c24;
    --paper: #ffffff;
  }
  * { margin: 0; padding: 0; box-sizing: border-box; }
  html, body {
    width: 1200px; height: 1200px; overflow: hidden;
    background: var(--backdrop);
    font-family: "Tinos", "Times New Roman", serif;
  }
  .card {
    position: absolute;
    left: 296px;
    width: 608px; height: 346px;
    border-radius: 9px;
    overflow: hidden;
    background: var(--paper);
  }
  .card--front { top: 233px; }
  .card--back  { top: 620px; }

  /* front */
  .front-header {
    position: absolute; left: 0; top: 0;
    width: 100%; height: 106px;
    background: var(--brand-blue);
  }
  .front-rule {
    position: absolute; left: 0; top: 106px;
    width: 383px; height: 9px;
    background: var(--band-dark);
  }
  .front-footer {
    position: absolute; left: 0; bottom: 0;
    width: 100%; height: 21px;
    background: var(--band-dark);
  }
  .brand {
    position: absolute; left: 38px; top: 40px;
    display: flex; align-items: center; gap: 8px;
    color: var(--logo-grey);
    font-weight: 700; font-size: 27px; line-height: 1;
  }
  .brand__mark {
    width: 22px; height: 22px;
    background: var(--logo-grey);
  }
  .name-plate {
    position: absolute; left: 383px; top: 87px;
    width: 225px; height: 69px;
    background: var(--plate-black);
    border-radius: 7px 0 0 7px;
    color: var(--paper);
    text-align: center;
  }
  .name-plate__name {
    position: absolute; left: 0; right: 0; top: 5px;
    font-size: 29px; line-height: 1.1; white-space: nowrap;
  }
  .name-plate__first { font-weight: 700; }
  .name-plate__role {
    position: absolute; left: 0; right: 0; top: 38px;
    font-size: 20px; line-height: 1.2;
  }
  .location {
    position: absolute; left: 22px; top: 209px;
    width: 140px; text-align: center;
    color: var(--ink);
  }
  .location__pin { display: block; margin: 0 auto; width: 26px; height: 37px; }
  .location__city { font-size: 28px; line-height: 1; margin-top: 11px; white-space: nowrap; }
  .divider {
    position: absolute; left: 169px; top: 195px;
    width: 4px; height: 100px;
    background: var(--ink); border-radius: 2px;
  }
  .phone {
    position: absolute; left: 194px; top: 227px;
    display: flex; align-items: center; gap: 16px;
    color: var(--ink); font-size: 28px; line-height: 1; white-space: nowrap;
  }
  .phone__icon { width: 31px; height: 33px; }

  /* back */
  .back-panel { position: absolute; inset: 0; }
  .back-brand {
    position: absolute; left: 0; right: 0; top: 140px;
    display: flex; justify-content: center; align-items: center; gap: 16px;
    color: var(--logo-grey);
    font-weight: 700; font-size: 64px; line-height: 1;
  }
  .back-brand__mark {
    width: 44px; height: 44px;
    background: var(--logo-grey);
  }
</style>
</head>
<body>

<section class="card card--front" aria-label="Business card front">
  <div class="front-header"></div>
  <div class="front-rule"></div>
  <div class="brand"><span class="brand__mark"></span><span>Quarneth</span></div>

  <div class="name-plate">
    <p class="name-plate__name"><span class="name-plate__first">Derek</span> Olstow</p>
    <p class="name-plate__role">Director</p>
  </div>

  <div class="location">
    <svg class="location__pin" viewBox="0 0 26 37" aria-hidden="true">
      <path d="M13 1C6.4 1 1 6.2 1 12.7c0 7.6 12 23.3 12 23.3s12-15.7 12-23.3C25 6.2 19.6 1 13 1z" fill="var(--pin-red)"/>
      <circle cx="13" cy="12.5" r="5" fill="#fff"/>
    </svg>
    <p class="location__city">Marlowby</p>
  </div>

  <div class="divider"></div>

  <div class="phone">
    <svg class="phone__icon" viewBox="0 0 31 33" aria-hidden="true">
      <path d="M5 6c-3 2-4 5-2 9 3 6 7 11 13 15 3 2 6 2 8 0l2-2c1-1 1-2 0-3l-4-3c-1-1-2-1-3 0l-2 2c-3-1-7-6-8-9l2-2c1-1 1-2 0-3L8 6C7 5 6 5 5 6z" fill="var(--ink)"/>
      <path d="M17 9a7 7 0 0 1 6 6" stroke="var(--ink)" stroke-width="2.2" fill="none" stroke-linecap="round"/>
      <path d="M18 4a12 12 0 0 1 10 10" stroke="var(--ink)" stroke-width="2.2" fill="none" stroke-linecap="round"/>
    </svg>
    <span class="phone__number">021 387 9415</span>
  </div>

  <div class="front-footer"></div>
</section>

<section class="card card--back" aria-label="Business card back">
  <svg class="back-panel" viewBox="0 0 608 346" preserveAspectRatio="none" aria-hidden="true">
    <polygon points="206,0 608,0 608,346 379,346" fill="var(--brand-blue)"/>
  </svg>
  <div class="back-brand"><span class="back-brand__mark"></span><span>Quarneth</span></div>
</section>

</body>
</html>
```